Create Lanternfield HR Business Cards.

Create Business Cards for Lanternfield HR. 2 sided and Would like the back to have the logo.

Info for Business Card:
Address: 4827 Millbrook Ave Suite 230 Cleveland, Ohio 44987
Office Number: 216-555-0143
Mobile: 216-555-0192

Website: www.lanternfieldhr.example

Target Market(s)

Small to medium size businesses

Industry/Entity Type

Human Resources

Contact Information for Business Card

Company logo and information

Font styles to use
Serif
Sans Serif

Requirements
Must have
• Info for Business Card: Address: 4827 Millbrook Ave Suite 230 Cleveland, Ohio 44987 Office Number: 216-555-0143 Mobile: 216-555-0192 Website: www.lanternfieldhr.example

```html
<!DOCTYPE html>
<html lang="en">
<head>
<meta charset="utf-8">
<title>Lanternfield HR Business Cards</title>
<link href="https://fonts.googleapis.com/css2?family=Inter:wght@400;600;700;800&display=swap" rel="stylesheet">
<style>
  :root {
    --stage: #f2f2f2;
    --orange: #ff8800;
    --navy: #252060;
    --white: #ffffff;
    --rule: #3a3a3a;
  }
  html, body {
    margin: 0;
    padding: 0;
    width: 1200px;
    height: 1000px;
    overflow: hidden;
    background: var(--stage);
    font-family: "Inter", Arial, sans-serif;
  }
  .canvas {
    position: relative;
    width: 1200px;
    height: 1000px;
  }
  .card {
    position: absolute;
    left: 294px;
    width: 613px;
    height: 352px;
    border-radius: 28px;
    overflow: hidden;
  }
  .card--front {
    top: 160px;
    background: var(--orange);
  }
  .card--back {
    top: 549px;
    background: var(--white);
    border: 1px solid #e2e2e2;
    box-sizing: border-box;
  }
  .front-brand {
    position: absolute;
    left: 356px;
    top: 252px;
    width: 165px;
    text-align: center;
    color: var(--white);
  }
  .front-brand__name {
    font-weight: 800;
    font-size: 19px;
    letter-spacing: 0.3px;
    white-space: nowrap;
    margin-left: -20px;
    margin-right: -20px;
  }
  .front-brand__web {
    margin-top: 8px;
    font-size: 16px;
    white-space: nowrap;
  }
  .front-brand__web b { font-weight: 700; }

  .back-brand {
    position: absolute;
    left: 70px;
    top: 100px;
    width: 200px;
    text-align: center;
  }
  .back-brand__dot {
    display: block;
    width: 44px;
    height: 44px;
    border-radius: 50%;
    background: var(--orange);
    margin: 0 auto 14px;
  }
  .back-brand__name {
    color: var(--navy);
    font-weight: 800;
    font-size: 24px;
    white-space: nowrap;
  }
  .divider {
    position: absolute;
    left: 305px;
    top: 88px;
    width: 1px;
    height: 176px;
    background: var(--rule);
  }
  .contact {
    position: absolute;
    left: 343px;
    top: 110px;
    color: var(--navy);
    font-size: 15px;
    line-height: 20px;
  }
  .contact__name {
    font-weight: 700;
    font-size: 17px;
    margin-bottom: 8px;
  }
  .contact__address { margin: 0 0 18px; }
  .contact__line {
    display: flex;
    align-items: center;
    gap: 4px;
  }
  .contact__line svg { flex: none; }
  .back-web {
    position: absolute;
    left: 0;
    right: 0;
    top: 311px;
    text-align: center;
    font-size: 17px;
    color: var(--navy);
  }
  .back-web b { color: var(--orange); font-weight: 700; }
</style>
</head>
<body>
<main class="canvas">
  <section class="card card--front" aria-label="Card front">
    <div class="front-brand">
      <div class="front-brand__name">LANTERNFIELD HR</div>
      <div class="front-brand__web"><b>lanternfieldhr</b>.example</div>
    </div>
  </section>

  <section class="card card--back" aria-label="Card back">
    <div class="back-brand">
      <span class="back-brand__dot"></span>
      <div class="back-brand__name">Lanternfield HR</div>
    </div>
    <div class="divider"></div>
    <div class="contact">
      <div class="contact__name">Lanternfield HR</div>
      <p class="contact__address">4827 Millbrook Ave Suite 230<br>Cleveland, Ohio 44987</p>
      <div class="contact__line">
        <svg width="10" height="11" viewBox="0 0 24 24" aria-hidden="true"><path fill="#ff8800" d="M6.6 10.8a15.1 15.1 0 0 0 6.6 6.6l2.2-2.2c.3-.3.7-.4 1-.2 1.1.4 2.3.6 3.6.6.6 0 1 .4 1 1V20c0 .6-.4 1-1 1C10.6 21 3 13.4 3 4c0-.6.4-1 1-1h3.5c.6 0 1 .4 1 1 0 1.3.2 2.5.6 3.6.1.3 0 .7-.2 1z"/></svg>
        <span>(216) 555-0143</span>
      </div>
      <div class="contact__line">
        <svg width="10" height="14" viewBox="0 0 10 14" aria-hidden="true"><rect x="1" y="0.8" width="8" height="12.4" rx="1.3" fill="none" stroke="#ff8800" stroke-width="1.6"/><rect x="4" y="10.3" width="2" height="1.3" fill="#ff8800"/></svg>
        <span>(216) 555-0192</span>
      </div>
    </div>
    <div class="back-web"><b>lanternfieldhr</b>.example</div>
  </section>
</main>
</body>
</html>
```